Graphic design for "How It Works" for VelmoraStyles.com*

VelmoraStyles.com website is for selling custom designer outfits for women and girls in all countries, customers can choose existing designs on this website and customize to their measurements. Customers can also provide their own designs and measurements and our expert designers and tailors get the outfit stitched and delivered to the customer.

We wanted to explain how this entire process works in 4 steps in the form of graphic design with little heading and text describing each step.

Step 1: Select Dress
Its time to choose the beauty you want to adorn yourself with. We have a wide collection of premium dresses, colours and accessories. There is something for everyone! All you need to do is pick. If you can’t find what you are looking for then you can share a picture of what you want, we will get it done whatever you want.

Step 2: Customization
Everyone is different; hence we realise the need for customization of the design and size. Here you select exactly how you want your dress to be. From sleeves to cuts, everything will be done as per your wish. Enter your measurements, lo and behold! You’re done. Leave your comments for even more customization.

Step 3: Designer Consultation
We as a user-friendly brand, aspire to provide the best of services to our clients. Our expert lady designers will help you for everything right from selecting of fabric to design of dress to necessary accessories. Our designers are just a call away!

Step 4: Stitch and Deliver
After you have placed your order, we confirm and verify the details. The boutique completes your order, sends it to us and we deliver it to your doorstep. We also have a team of designers in-house to cater to your premium dressing needs.

```html
<!DOCTYPE html>
<html lang="en">
<head>
<meta charset="utf-8">
<title>How it works</title>
<link rel="stylesheet" href="https://fonts.googleapis.com/css2?family=Fira+Sans:wght@800&family=Roboto+Condensed:wght@700&family=Lato:wght@400&display=swap">
<style>
  :root {
    --bg: #ffffff;
    --ink: #2a2a2a;
    --title: #d8245d;
    --pink: #d42a78;
    --purple: #6a45a0;
    --blue: #2a6db4;
    --teal: #2a9a8a;
    --green: #4cb86a;
    --olive: #a49a3c;
    --orange: #ea8e32;
    --arrow: #9a9a9a;
    --icon-area: #ececec;
  }
  * { margin: 0; padding: 0; box-sizing: border-box; }
  html, body { width: 1200px; height: 370px; overflow: hidden; background: var(--bg); }
  .canvas { position: relative; width: 1200px; height: 370px; overflow: hidden; }
  .flow { position: absolute; inset: 0; }
  .page-title {
    position: absolute; left: 0; width: 1200px; top: 6px;
    text-align: center;
    font: 800 37px/44px "Fira Sans", sans-serif;
    color: var(--title);
    letter-spacing: -0.5px;
    text-shadow: 1px 2px 2px rgba(0,0,0,0.25);
  }
  .step { position: absolute; text-align: center; }
  .step-heading {
    font: 700 27px/32px "Roboto Condensed", sans-serif;
    display: inline-block;
    -webkit-background-clip: text; background-clip: text;
    color: transparent;
  }
  .step-text {
    margin-top: 6px;
    font: 400 13.2px/16px "Lato", sans-serif;
    color: var(--ink);
    white-space: nowrap;
  }
  .step--select { left: 6px; width: 300px; top: 210px; }
  .step--select .step-heading { background-image: linear-gradient(90deg, var(--pink), var(--purple)); }
  .step--custom { left: 286px; width: 330px; top: 62px; }
  .step--custom .step-heading { background-image: linear-gradient(90deg, var(--purple), var(--blue)); }
  .step--consult { left: 600px; width: 302px; top: 210px; }
  .step--consult .step-heading { background-image: linear-gradient(90deg, var(--blue), var(--teal)); }
  .step--deliver { left: 886px; width: 300px; top: 62px; }
  .step--deliver .step-heading { background-image: linear-gradient(90deg, var(--green), var(--olive)); }
</style>
</head>
<body>
<div class="canvas">
  <svg class="flow" width="1200" height="370" viewBox="0 0 1200 370">
    <defs>
      <linearGradient id="ring-select" x1="0" y1="0" x2="1" y2="0">
        <stop offset="0" stop-color="var(--pink)"/><stop offset="1" stop-color="var(--purple)"/>
      </linearGradient>
      <linearGradient id="ring-custom" x1="0" y1="0" x2="1" y2="0">
        <stop offset="0" stop-color="var(--purple)"/><stop offset="1" stop-color="var(--blue)"/>
      </linearGradient>
      <linearGradient id="ring-consult" x1="0" y1="0" x2="1" y2="0">
        <stop offset="0" stop-color="var(--blue)"/><stop offset="1" stop-color="var(--green)"/>
      </linearGradient>
      <linearGradient id="ring-deliver" x1="0" y1="0" x2="1" y2="0">
        <stop offset="0" stop-color="var(--green)"/><stop offset="1" stop-color="var(--orange)"/>
      </linearGradient>
      <marker id="arrow-head" viewBox="0 0 10 10" refX="8" refY="5" markerWidth="7" markerHeight="7" orient="auto">
        <path d="M0 0 L10 5 L0 10 L3 5 Z" fill="var(--arrow)"/>
      </marker>
    </defs>

    <g class="connectors" fill="none" stroke="var(--arrow)" stroke-width="1.3" stroke-dasharray="3 2.5" marker-end="url(#arrow-head)">
      <line x1="227" y1="177" x2="374" y2="262"/>
      <line x1="527" y1="260" x2="676" y2="174"/>
      <line x1="816" y1="177" x2="963" y2="262"/>
    </g>

    <g class="step-badge">
      <circle cx="156" cy="131" r="71" fill="none" stroke="url(#ring-select)" stroke-width="7"/>
      <circle cx="156" cy="131" r="52" fill="var(--icon-area)" role="img" aria-label="Dress with a checklist icon"/>
    </g>
    <g class="step-badge">
      <circle cx="451" cy="292" r="71" fill="none" stroke="url(#ring-custom)" stroke-width="7"/>
      <circle cx="451" cy="292" r="52" fill="var(--icon-area)" role="img" aria-label="Tailoring scissors icon"/>
    </g>
    <g class="step-badge">
      <circle cx="745" cy="131" r="71" fill="none" stroke="url(#ring-consult)" stroke-width="7"/>
      <circle cx="745" cy="131" r="52" fill="var(--icon-area)" role="img" aria-label="Support headset with speech bubble icon"/>
    </g>
    <g class="step-badge">
      <circle cx="1040" cy="292" r="71" fill="none" stroke="url(#ring-deliver)" stroke-width="7"/>
      <circle cx="1040" cy="292" r="52" fill="var(--icon-area)" role="img" aria-label="Sewing machine and delivered parcel icon"/>
    </g>
  </svg>

  <h1 class="page-title">How it works</h1>

  <section class="step step--select">
    <h2 class="step-heading">Select Dress</h2>
    <p class="step-text">Its time to choose the beauty you want to adorn<br>yourself with. We have a wide collection of<br>premium dresses, colours and accessories. There<br>is something for everyone! All you need to do is<br>pick. If you can’t find what you are looking for<br>then you can share a picture of what you want, we<br>will get it done whatever you want.</p>
  </section>

  <section class="step step--custom">
    <h2 class="step-heading">Customization</h2>
    <p class="step-text">Everyone is different; hence we realise the need for<br>customization of the design and size. Here you select<br>exactly how you want your dress to be. From sleeves<br>to cuts, everything will be done as per your wish. Enter<br>your measurements, lo and behold! You’re done. Leave<br>your comments for even more customization.</p>
  </section>

  <section class="step step--consult">
    <h2 class="step-heading">Designer Consultation</h2>
    <p class="step-text">We as a user-friendly brand, aspire to provide<br>the best of services to our clients. Our expert<br>lady designers will help you for everything<br>right from selecting of fabric to design of dress<br>to necessary accessories. Our designers are<br>just a call away!</p>
  </section>

  <section class="step step--deliver">
    <h2 class="step-heading">Stitch and Deliver</h2>
    <p class="step-text">After you have placed your order, we confirm and<br>verify the details. The boutique completes your<br>order, sends it to us and we deliver it to your<br>doorstep. We also have a team of designers in-<br>house to cater to your premium dressing needs.</p>
  </section>
</div>
</body>
</html>
```